Company Profile for Academic and Study Abroad Services

I am looking for Power Point Design for company Profile . the company is academic and study abroad services. you can visit the website which is www.korvelan.ae . the colour i prefer is Dark Blue + White + Black . you can find all the content for power point and logo and some picture i need you to add it.

Target Market(s)

Students who wants to study abroad. Universities . Learning centre.

Industry/Entity Type

Education

Font styles to use
Serif
Sans Serif

Colors
0555a3
ffffff
000000
aaaaaa

Requirements
Must have
• Must Have Images for each slides.
Nice to have
• infographic. Images related to the study abroad

```html
<!DOCTYPE html>
<html lang="en">
<head>
<meta charset="utf-8">
<title>Korvelan – Company Profile Slides</title>
<link href="https://fonts.googleapis.com/css2?family=Open+Sans:wght@400;600;700&family=Oswald:wght@500&display=swap" rel="stylesheet">
<style>
:root{
  --board-a:#5f5f5f;
  --board-b:#9c9c9c;
  --navy:#0a0a9a;
  --brand-blue:#0b3c7d;
  --chart-navy:#1b2f66;
  --header-grey:#555555;
  --slide-white:#f7f7f7;
  --ink:#111111;
  --yellow:#f5c02a;
  --icon-grey:#d4d4d4;
  --red:#e8524c;
  --light-grey:#dcdcdc;
  --dark-slide:#3f3f3f;
  --option-grey:#5a5a5a;
  --photo-dark:#34323a;
  --photo-mid:#4a4450;
}
*{box-sizing:border-box;margin:0;padding:0}
html,body{width:1200px;height:1200px;overflow:hidden}
body{
  background:linear-gradient(90deg,var(--board-a) 0%,var(--board-b) 100%);
  font-family:"Open Sans",Arial,sans-serif;
  color:var(--ink);
  position:relative;
}
.slide{position:absolute;width:540px;height:306px;overflow:hidden;background:var(--slide-white)}
.col-1{left:51px}.col-2{left:615px}
.row-1{top:141px}.row-2{top:472px}.row-3{top:801px}

.slide-header{position:absolute;left:0;top:0;width:100%;height:54px;background:var(--header-grey)}
.slide-header h2{position:absolute;left:41px;top:18px;color:#fff;font-size:14px;font-weight:700;letter-spacing:.2px}
.slide-number{position:absolute;right:0;top:0;width:111px;height:100%;background:var(--navy);
  color:#1a1a40;font-size:25px;display:flex;align-items:center;justify-content:center}

/* cover */
.cover-photo{position:absolute;inset:0;background:linear-gradient(100deg,#efe8d6 0%,#8a847a 35%,#3a3836 65%,#4a4744 100%)}
.brand-mark{position:absolute;left:28px;top:34px;display:flex;align-items:center;gap:5px}
.brand-mark .square{width:10px;height:10px;background:var(--brand-blue)}
.brand-mark span{font-size:13px;font-weight:700;color:var(--brand-blue)}
.cover-title{position:absolute;left:177px;top:212px;color:#fff;font-size:15px;font-weight:700;line-height:20px}

/* who we are */
.feature{position:absolute;width:115px}
.feature .head{display:flex;align-items:center;gap:8px;height:50px}
.feature .num{font-family:"Oswald",sans-serif;font-size:46px;color:var(--yellow);line-height:1}
.feature p{font-size:6px;font-weight:700;line-height:7.5px;margin-top:2px}
.divider{position:absolute;left:335px;top:72px;width:2px;height:216px;background:#dddddd}
.headline{position:absolute;left:358px;top:86px;width:165px}
.headline h3{font-size:23px;font-weight:400;line-height:1}
.headline .sub{font-size:8px;font-weight:700;margin-top:2px}
.headline p{font-size:5px;font-weight:700;line-height:6.5px;margin-top:16px}
.headline p + p{margin-top:7px}

/* what we do */
.steps{position:absolute;left:84px;top:90px;width:370px;height:124px}
.step{position:absolute;top:0;height:124px;color:#fff;text-align:center}
.step h4{font-size:17px;font-weight:400;margin-top:24px}
.step p{font-size:5px;font-weight:700;line-height:6px;margin:5px 14px 0}
.steps-note{position:absolute;left:86px;top:230px;width:370px;text-align:center;font-size:6.5px;font-weight:700;line-height:9px}

/* chart */
.chart{position:absolute;left:0;top:0}
.legend{position:absolute;top:243px;display:flex;gap:5px;width:105px}
.legend i{display:block;width:15px;height:15px;flex:none}
.legend p{width:80px;font-size:5px;font-weight:700;line-height:6px}

/* why choose */
.option-a{position:absolute;left:0;top:0;width:270px;height:100%;background:var(--brand-blue)}
.option-b{position:absolute;left:270px;top:0;width:270px;height:100%;background:var(--option-grey)}
.why-title{position:absolute;top:18px;width:100%;text-align:center;color:#fff;font-size:14px;font-weight:700}
.option{position:absolute;top:60px;width:200px;text-align:center;color:#fff}
.option h3{font-size:26px;font-weight:400;letter-spacing:5px;line-height:1}
.option .sub{font-size:8.5px;font-weight:700;margin-top:2px}
.option hr{width:66px;margin:12px auto 0;border:0;border-top:2px solid #6f9bd6}
.option-b-text hr{border-top-color:#9a9a9a}
.option p{font-size:5.5px;font-weight:700;line-height:7px;margin-top:12px}
.stadium-photo{position:absolute;left:180px;top:186px;width:169px;height:111px;
  background:linear-gradient(180deg,var(--photo-dark) 0%,var(--photo-mid) 100%)}

/* closing */
.closing{background:var(--dark-slide)}
.closing-band{position:absolute;left:0;top:59px}
.closing-brand{position:absolute;left:104px;top:80px;display:flex;align-items:center;gap:5px}
.closing-brand .square{width:9px;height:9px;background:var(--brand-blue)}
.closing-brand span{font-size:12px;font-weight:700;color:var(--brand-blue)}
.closing h2{position:absolute;left:232px;top:158px;color:#fff;font-size:17px;font-weight:400}
.contact{position:absolute;left:232px;top:189px;color:#fff;font-size:6px;font-weight:700;line-height:7px}
.contact .gap{margin-top:6px}
</style>
</head>
<body>

<section class="slide col-1 row-1 cover">
  <div class="cover-photo" role="img" aria-label="Group photo of smiling students sitting together on a staircase"></div>
  <div class="brand-mark"><i class="square"></i><span>KORVELAN</span></div>
  <h1 class="cover-title">KORVELAN<br>Universities<br>Entrance Services</h1>
</section>

<section class="slide col-2 row-1 who-we-are">
  <header class="slide-header"><h2>WHO WE ARE</h2><div class="slide-number">01</div></header>
  <div class="feature" style="left:41px;top:80px">
    <div class="head">
      <svg width="42" height="36" viewBox="0 0 42 36"><rect x="0" y="20" width="9" height="16" fill="var(--icon-grey)"/><rect x="12" y="12" width="9" height="24" fill="var(--icon-grey)"/><rect x="24" y="3" width="9" height="33" fill="var(--icon-grey)"/></svg>
      <span class="num">01</span>
    </div>
    <p>We guide students toward the right universities abroad.</p>
  </div>
  <div class="feature" style="left:176px;top:80px">
    <div class="head">
      <svg width="42" height="40" viewBox="0 0 40 40"><g fill="var(--icon-grey)"><circle cx="20" cy="20" r="13"/><rect x="16" y="2" width="8" height="36"/><rect x="2" y="16" width="36" height="8"/><rect x="16" y="2" width="8" height="36" transform="rotate(45 20 20)"/><rect x="16" y="2" width="8" height="36" transform="rotate(-45 20 20)"/></g><circle cx="20" cy="20" r="6" fill="var(--slide-white)"/></svg>
      <span class="num">02</span>
    </div>
    <p>Clear steps from first enquiry to final enrolment.</p>
  </div>
  <div class="feature" style="left:41px;top:182px">
    <div class="head">
      <svg width="46" height="40" viewBox="0 0 46 40"><circle cx="23" cy="12" r="10" fill="var(--icon-grey)"/><path d="M2 40 Q2 23 23 23 Q44 23 44 40Z" fill="var(--icon-grey)"/></svg>
      <span class="num">03</span>
    </div>
    <p>Personal advisers support every student and family.</p>
  </div>
  <div class="feature" style="left:176px;top:182px">
    <div class="head">
      <svg width="42" height="40" viewBox="0 0 42 40"><circle cx="16" cy="16" r="12" fill="none" stroke="var(--icon-grey)" stroke-width="6"/><rect x="26" y="24" width="8" height="18" fill="var(--icon-grey)" transform="rotate(-45 30 33)"/></svg>
      <span class="num">04</span>
    </div>
    <p>We search programmes that match goals and budget.</p>
  </div>
  <div class="divider"></div>
  <div class="headline">
    <h3>HEADLINE</h3>
    <div class="sub">Lorem Ipsum Dolor Sit Amet</div>
    <p>Korvelan helps students plan study abroad with care. We compare universities, check entry needs, prepare documents and follow every application until an offer arrives.</p>
    <p>Our team works with universities and learning centres across many countries, giving students honest advice and steady support from the first meeting to arrival.</p>
  </div>
</section>

<section class="slide col-1 row-2 what-we-do">
  <header class="slide-header" style="height:52px"><h2>WHAT WE DO</h2><div class="slide-number" style="width:110px">02</div></header>
  <div class="steps">
    <svg width="370" height="124" viewBox="0 0 370 124" style="position:absolute;left:0;top:0">
      <rect x="0" y="0" width="370" height="124" rx="7" fill="#6d6c72"/>
      <path d="M0 7 Q0 0 7 0 H247 L257 10 V124 H7 Q0 124 0 117Z" fill="#a8a7ad"/>
      <path d="M0 7 Q0 0 7 0 H123 L133 10 V124 H7 Q0 124 0 117Z" fill="#d4d4d6"/>
    </svg>
    <div class="step" style="left:0;width:123px"><h4>STEP 1</h4><p>Meet an adviser, share your goals, grades and preferred study destinations.</p></div>
    <div class="step" style="left:123px;width:124px"><h4>STEP 2</h4><p>Receive a shortlist of universities and programmes that suit your profile.</p></div>
    <div class="step" style="left:247px;width:123px"><h4>STEP 3</h4><p>Apply with our help, secure your offer and prepare for departure.</p></div>
  </div>
  <p class="steps-note">Lorem ipsum dolor sit amet, ius exerci corpora eu. Per ne meis vocent iudicabit, in oratio graeci atomorum vim, vide habemus docendi ut eam. Cu dolor salutatus efficiendi nam. Debet quaeque nec te. Omittam reprehendunt eu mea, vocent aperiri eumet, ut ius summo dignissim. Pro ne ubique voluptaria, te alia lorem perfecto vix.</p>
</section>

<section class="slide col-2 row-2 education-levels">
  <header class="slide-header" style="height:52px"><h2>EDUCATION LEVELS</h2><div class="slide-number" style="width:110px">03</div></header>
  <svg class="chart" width="540" height="306" viewBox="0 0 540 306" font-family="Open Sans, sans-serif" font-size="7" font-weight="700">
    <g stroke="#cfcfcf" stroke-dasharray="2 2" stroke-width="0.7" fill="none">
      <line x1="83" y1="88" x2="478" y2="88"/><line x1="83" y1="120" x2="478" y2="120"/>
      <line x1="83" y1="151" x2="478" y2="151"/><line x1="83" y1="183" x2="478" y2="183"/>
      <line x1="119" y1="88" x2="119" y2="214"/><line x1="155" y1="88" x2="155" y2="214"/>
      <line x1="191" y1="88" x2="191" y2="214"/><line x1="227" y1="88" x2="227" y2="214"/>
      <line x1="263" y1="88" x2="263" y2="214"/><line x1="298" y1="88" x2="298" y2="214"/>
      <line x1="334" y1="88" x2="334" y2="214"/><line x1="370" y1="88" x2="370" y2="214"/>
      <line x1="406" y1="88" x2="406" y2="214"/><line x1="442" y1="88" x2="442" y2="214"/>
      <line x1="478" y1="88" x2="478" y2="214"/>
    </g>
    <path d="M83 167 L119 146 L155 162 L191 151 L227 138 L263 159 L298 167 L334 156 L370 138 L406 120 L442 131 L478 109 V214 H83Z" fill="var(--chart-navy)"/>
    <line x1="83" y1="214" x2="478" y2="214" stroke="#888" stroke-width="0.7"/>
    <g fill="#222" text-anchor="end"><text x="71" y="91">400</text><text x="71" y="123">300</text><text x="71" y="154">200</text><text x="71" y="186">100</text></g>
    <g fill="#222" text-anchor="middle">
      <text x="83" y="226">A</text><text x="119" y="226">B</text><text x="155" y="226">C</text><text x="191" y="226">D</text>
      <text x="227" y="226">E</text><text x="263" y="226">F</text><text x="298" y="226">G</text><text x="334" y="226">H</text>
      <text x="370" y="226">I</text><text x="406" y="226">J</text><text x="442" y="226">K</text><text x="478" y="226">L</text>
    </g>
    <path d="M138 127 H172 V146 H160 L155 151 L150 146 H138Z" fill="var(--navy)"/><circle cx="155" cy="162" r="2.5" fill="#777"/>
    <path d="M281 132 H315 V151 H303 L298 156 L293 151 H281Z" fill="var(--red)"/><circle cx="298" cy="167" r="2.5" fill="#777"/>
    <path d="M389 83 H423 V102 H411 L406 107 L401 102 H389Z" fill="var(--light-grey)"/><circle cx="406" cy="120" r="2.5" fill="#777"/>
  </svg>
  <div class="legend" style="left:79px"><i style="background:var(--navy)"></i><p>Undergraduate study for school leavers.</p></div>
  <div class="legend" style="left:196px"><i style="background:var(--red)"></i><p>Postgraduate and master study abroad.</p></div>
  <div class="legend" style="left:313px"><i style="background:var(--light-grey)"></i><p>Foundation and language courses.</p></div>
</section>

<section class="slide col-1 row-3 why-choose">
  <div class="option-a"></div>
  <div class="option-b"></div>
  <h2 class="why-title">WHY CHOOSE KORVELAN</h2>
  <div class="option" style="left:35px">
    <h3>OPTION A</h3>
    <div class="sub">Lorem Ipsum Dolor Sit Amet</div>
    <hr>
    <p>Korvelan gives every student a dedicated adviser, clear timelines and honest guidance on universities, visas and scholarships, so each application is strong and complete.</p>
  </div>
  <div class="option option-b-text" style="left:305px">
    <h3>OPTION B</h3>
    <div class="sub">Lorem Ipsum Dolor Sit Amet</div>
    <hr>
    <p>We work with universities and learning centres in many countries, opening more choices for students and helping them settle well once they arrive abroad.</p>
  </div>
  <div class="stadium-photo" role="img" aria-label="Photo of a floodlit stadium at night"></div>
</section>

<section class="slide col-2 row-3 closing">
  <svg class="closing-band" width="290" height="63" viewBox="0 0 290 63"><path d="M0 0 H290 L240 63 H0Z" fill="#e6e6e6"/></svg>
  <div class="closing-brand"><i class="square"></i><span>KORVELAN</span></div>
  <h2>BE AMONG THE BEST</h2>
  <div class="contact">
    <div>Harbour Road . Meridian Sports Arena</div>
    <div>Meridian Club Suite - 14, 3rd Floor</div>
    <div>UAE- Abu Dhabi</div>
    <div>+971 2 000 1234 | +971 50 000 1111 +971 52 000 2222 | +971 50 000 3333</div>
    <div>www.korvelan.ae</div>
    <div>info@korvelan.ae</div>
    <div class="gap">Facebook: korvelan.ae</div>
    <div>Twitter: korvelan_ae</div>
    <div>Instagram: korvelan.ae</div>
  </div>
</section>

</body>
</html>
```